galactic arcade 80s vibes - jewelry company

I am looking for someone to build me a website for my jewelry company - I am going for an 80s retro GALACTIC arcade vibe. I want it to feel old school, be brightly colored (purples, greens, etc) encompass planets, stars, or milky way type vibes. My company is called LunoVix - it is zodiac signs & angel number jewelry. I want the website to open up as galaxy and my logo/name to pop up in the center of the screen and then go to the main page.

Industry/Entity Type

jewelry

Coding

Coded - Design and coding required

Number of Pages Required

1 page

Font styles to use
Other font styles liked:
• retro

Colors
0094D4
00A9DD
6FCCEA
C7EBF8
E9F6FB
00AB8E
00BBA5
67D7C9
C6EFE9
E9F9F6
59FF00
82FF00
B8FF75
E3FFCB
F4FFEA
FFF300
FFF600
FEFA6F
FFFEC7
FFFEE8
FFC000
F8CF3A
FAE287
FDF2CF
FEFAEE
E54698
E96AAD
F1A4CE
F9D9EA
FCEFF6
A7469A
B969AE
D3A5CF
EDDBEB
F8F0F9
6B429C
8869AF
B7A5CE
E3DAEB
F3F0F8

```html
<!DOCTYPE html>
<html lang="en">
<head>
<meta charset="utf-8">
<title>LunoVix — Zodiac &amp; Angel Number Jewelry</title>
<link rel="stylesheet" href="https://fonts.googleapis.com/css2?family=Josefin+Sans:wght@300;400;600;700&display=swap">
<style>
:root{
  --green:#59FF00;
  --white:#ffffff;
  --black:#000000;
  --muted:#bdbdbd;
  --night-1:#05081e;
  --night-2:#14206a;
  --night-3:#2a3aa8;
  --violet:#6B429C;
  --magenta:#A7469A;
  --pink:#E54698;
  --orange:#FFC000;
  --card-dark:#3d3d3d;
  --card-light:#d7d7d7;
  --ink:#111111;
  --grey-text:#7d7d7d;
  --font:"Josefin Sans", sans-serif;
}
*{margin:0;padding:0;box-sizing:border-box}
html,body{width:1200px;height:4048px;overflow:hidden}
body{position:relative;background:var(--black);color:var(--white);font-family:var(--font)}
.abs{position:absolute}
.center{text-align:center}
.btn{position:absolute;display:flex;align-items:center;justify-content:center;border:2px solid var(--white);border-radius:30px;color:var(--white);font-size:17px;font-weight:400;height:60px}
.eyebrow{color:var(--green);font-size:22px;font-weight:400}
.h2{font-size:44px;font-weight:600;letter-spacing:1px}
.lead{font-size:20px;line-height:30px;color:#cfcfcf;font-weight:300}

/* hero */
.hero{position:absolute;left:0;top:0;width:1200px;height:705px;background:radial-gradient(ellipse at 50% 30%,var(--night-3) 0%,var(--night-2) 45%,var(--night-1) 100%)}
.hero-ridge{position:absolute;left:0;top:560px;width:1200px;height:145px;background:linear-gradient(180deg,rgba(20,20,60,0) 0%,#0d0d26 60%,#050510 100%)}
.brand-mark{position:absolute;left:91px;top:19px;width:142px;height:142px;border-radius:50%;background:#3b2d70;display:flex;align-items:center;justify-content:center;color:var(--green);font-size:26px;font-weight:700}
.nav{position:absolute;top:46px;left:643px;display:flex;gap:46px;font-size:15px}
.nav a{color:var(--white);text-decoration:none;padding-bottom:8px}
.nav a.active{color:var(--green);border-bottom:2px solid var(--green)}
.social{display:flex;gap:22px}
.social span{display:block;width:17px;height:17px;border:2px solid var(--white);border-radius:50%}
.hero-title{position:absolute;left:0;width:1200px;top:228px;text-align:center;color:var(--green);font-size:128px;font-weight:700;letter-spacing:4px}
.hero-tag{position:absolute;left:0;width:1200px;top:394px;text-align:center;font-size:19px}

/* about */
.about-art{position:absolute;left:3px;top:760px;width:610px;height:585px;background:radial-gradient(circle at 50% 40%,#ffd23a 0%,#ff7a3a 25%,#e54698 42%,#2a1f6e 70%,#0b1040 100%)}
.about-glow{position:absolute;left:613px;top:760px;width:587px;height:630px;background:radial-gradient(ellipse at 95% 90%,#6e1d10 0%,#2a0a08 25%,#000 55%)}

/* zodiac */
.zodiac-bg{position:absolute;left:0;top:1350px;width:1200px;height:480px;background:radial-gradient(ellipse at 70% 60%,#4a1a55 0%,#1c0c2e 45%,#000 85%)}
.arrow-box{position:absolute;top:1395px;width:28px;height:28px;border:1.5px solid var(--white);display:flex;align-items:center;justify-content:center}
.sign{position:absolute;top:1568px;width:176px;text-align:center}
.sign .glyph{height:100px;display:flex;align-items:center;justify-content:center;font-size:46px;font-family:"Segoe UI Symbol","Noto Sans Symbols",sans-serif}
.sign .blob{width:102px;height:98px;border-radius:50% 46% 52% 48%;background:var(--green);display:flex;align-items:center;justify-content:center}
.sign .name{font-size:24px;margin-top:18px}
.sign .desc{font-size:14px;line-height:19px;margin-top:12px}
.sign.active .name{color:var(--green)}

/* services */
.card{position:absolute;top:2094px;width:327px;height:330px;border-radius:4px;text-align:center;padding-top:38px}
.card.dark{background:radial-gradient(ellipse at 50% 110%,#6d8596 0%,#4a4a4a 40%,var(--card-dark) 100%)}
.card.light{background:radial-gradient(ellipse at 50% 110%,#a9c4d6 0%,#d2d2d2 40%,var(--card-light) 100%)}
.card h3{font-size:21px;font-weight:400;margin-top:18px}
.card p{font-size:14px;line-height:19px;margin:16px auto 0;width:255px}
.card.dark h3{color:var(--green)}
.card.dark p{color:#eee}
.card.light h3{color:var(--ink)}
.card.light p{color:var(--grey-text)}

/* jewelry */
.jewel-card{position:absolute;left:613px;top:2831px;width:237px;height:413px;background:var(--white);border-radius:3px}
.jewel{position:absolute;top:2859px;width:220px;text-align:center}
.jewel .photo{width:110px;height:196px;margin:0 auto;border-radius:40px 40px 50px 50px}
.jewel .photo.gold{background:linear-gradient(180deg,#f2dcc4,#d8a77f 60%,#f6e7d6)}
.jewel .photo.silver{background:linear-gradient(180deg,#f2f2f2,#b8b8b8 60%,#e6e6e6)}
.jewel .name{font-size:24px;margin-top:38px}
.jewel .desc{font-size:14px;line-height:19px;margin-top:10px}
.jewel .cart{font-size:16px;font-weight:600;margin-top:26px;display:flex;align-items:center;justify-content:center;gap:10px}
.jewel.on-light .name{color:var(--ink)}
.jewel.on-light .desc{color:var(--grey-text)}
.jewel.on-light .cart{color:var(--ink)}

/* contact */
.contact-bg{position:absolute;left:0;top:3318px;width:1200px;height:260px;background:radial-gradient(ellipse at 10% 50%,#5a1f0c 0%,#1d0a12 35%,#06060c 70%)}
.planet{position:absolute;left:28px;top:3327px;width:226px;height:226px;border-radius:50%;background:radial-gradient(circle at 60% 35%,#6b7fa0 0%,#7a4a36 45%,#b3451a 75%,#3a120a 100%)}
.field{position:absolute;top:3440px;width:378px;border-bottom:1px solid #9a9a9a;font-size:14px;padding:0 0 16px 14px;color:#dcdcdc}

/* footer */
.footer-bg{position:absolute;left:0;top:3578px;width:1200px;height:470px;background:radial-gradient(ellipse at 60% 30%,#2b1630 0%,#120a18 45%,#050508 90%)}
.rule{position:absolute;left:85px;width:1030px;height:1px;background:#8a8a8a}
.footer-links{position:absolute;top:3864px;left:0;width:1200px;display:flex;justify-content:center;gap:44px;font-size:15px}
</style>
</head>
<body>

<!-- Hero -->
<section class="hero" role="img" aria-label="Starry night sky with shooting stars above dark mountains"></section>
<div class="hero-ridge"></div>
<div class="brand-mark">LunoVix</div>
<nav class="nav">
  <a class="active">Home</a><a>About</a><a>Services</a><a>Contact</a>
  <div class="social" aria-label="Social links"><span></span><span></span><span></span></div>
</nav>
<h1 class="hero-title">LUNOVIX</h1>
<p class="hero-tag">LunoVix is zodiac signs &amp; angel number jewelry.</p>
<a class="btn" style="left:502px;top:446px;width:196px">Discover More</a>

<!-- About -->
<div class="about-glow"></div>
<div class="about-art" role="img" aria-label="Retro neon palm tree in front of a striped synthwave sunset"></div>
<p class="eyebrow abs" style="left:613px;top:850px">About Us</p>
<h2 class="h2 abs" style="left:613px;top:886px">Welcome to LunoVix</h2>
<p class="abs" style="left:613px;top:952px;width:510px;font-size:20px;line-height:29px;color:#d6d6d6;font-weight:300">Lorem ipsum dolor sit amet, consectetur adipiscing elit. Donec nec egestas tellus, et condimentum est. Aliquam interdum sapien porta mauris interdum, a hendrerit risus condimentum. Donec viverra augue ac tristique mattis. Nulla non purus mi. Aenean enim nisi, luctus eget mi id, finibus gravida ex.</p>
<a class="btn" style="left:612px;top:1187px;width:160px">Learn More</a>

<!-- Zodiac -->
<div class="zodiac-bg" role="img" aria-label="Purple milky way nebula"></div>
<p class="eyebrow abs" style="left:85px;top:1393px">Zodiac Sign</p>
<h2 class="h2 abs" style="left:85px;top:1430px">Choose Your Zodiac Sign</h2>
<p class="lead abs" style="left:85px;top:1491px;width:760px">Lorem ipsum dolor sit amet, consectetur adipiscing elit. Donec nec egestas tellus, et condimentum est.</p>
<div class="arrow-box" style="left:1043px"><svg width="10" height="12" viewBox="0 0 10 12"><path d="M7 1 L2 6 L7 11" fill="none" stroke="#fff" stroke-width="1.6"/></svg></div>
<div class="arrow-box" style="left:1086px"><svg width="10" height="12" viewBox="0 0 10 12"><path d="M3 1 L8 6 L3 11" fill="none" stroke="#fff" stroke-width="1.6"/></svg></div>

<div class="sign active" style="left:72px"><div class="glyph"><div class="blob">&#9800;&#xFE0E;</div></div><p class="name">Aries</p><p class="desc">Lorem ipsum dolor<br>sit amet</p></div>
<div class="sign" style="left:248px"><div class="glyph">&#9801;&#xFE0E;</div><p class="name">Taurus</p><p class="desc">Lorem ipsum dolor<br>sit amet</p></div>
<div class="sign" style="left:424px"><div class="glyph">&#9802;&#xFE0E;</div><p class="name">Gemini</p><p class="desc">Lorem ipsum dolor<br>sit amet</p></div>
<div class="sign" style="left:600px"><div class="glyph">&#9803;&#xFE0E;</div><p class="name">Cancer</p><p class="desc">Lorem ipsum dolor<br>sit amet</p></div>
<div class="sign" style="left:776px"><div class="glyph">&#9804;&#xFE0E;</div><p class="name">Leo</p><p class="desc">Lorem ipsum dolor<br>sit amet</p></div>
<div class="sign" style="left:952px"><div class="glyph">&#9805;&#xFE0E;</div><p class="name">Virgo</p><p class="desc">Lorem ipsum dolor<br>sit amet</p></div>

<!-- Services -->
<p class="eyebrow abs center" style="left:0;width:1200px;top:1895px">Our Services</p>
<h2 class="h2 abs center" style="left:0;width:1200px;top:1930px">Services We offer</h2>
<p class="lead abs center" style="left:260px;width:680px;top:1994px">Lorem ipsum dolor sit amet, consectetur adipiscing elit. Donec nec egestas tellus, et condimentum est.</p>

<div class="card dark" style="left:85px">
  <svg width="110" height="96" viewBox="0 0 110 96" fill="none" stroke="#fff" stroke-width="2.4">
    <circle cx="58" cy="50" r="22"/><ellipse cx="58" cy="52" rx="38" ry="11" transform="rotate(-14 58 52)"/>
    <path d="M14 6 l3 8 8 3 -8 3 -3 8 -3 -8 -8 -3 8 -3z"/><path d="M92 2 l2 6 6 2 -6 2 -2 6 -2 -6 -6 -2 6 -2z"/><path d="M12 72 l2 6 6 2 -6 2 -2 6 -2 -6 -6 -2 6 -2z"/>
  </svg>
  <h3>Enter Service</h3>
  <p>Curabitur cursus sapien pharetra pretium suscipit. Etiam eu neque rhoncus, eleifend ex ut, ornare leo. Cras ac orci orci. Proin mattis nisi consequat</p>
</div>
<div class="card light" style="left:438px">
  <svg width="110" height="96" viewBox="0 0 110 96" fill="none" stroke="#111" stroke-width="2.4">
    <path d="M30 20 L58 30 L50 58 L82 52 L88 24 L58 30"/><circle cx="30" cy="20" r="3" fill="#111"/><circle cx="58" cy="30" r="3" fill="#111"/><circle cx="50" cy="58" r="3" fill="#111"/><circle cx="82" cy="52" r="3" fill="#111"/><circle cx="88" cy="24" r="3" fill="#111"/>
    <path d="M24 76 l3 8 8 3 -8 3 -3 8 -3 -8 -8 -3 8 -3z"/><path d="M94 62 l2 6 6 2 -6 2 -2 6 -2 -6 -6 -2 6 -2z"/>
  </svg>
  <h3>Enter Service</h3>
  <p>Curabitur cursus sapien pharetra pretium suscipit. Etiam eu neque rhoncus, eleifend ex ut, ornare leo. Cras ac orci orci. Proin mattis nisi consequat</p>
</div>
<div class="card light" style="left:789px">
  <svg width="110" height="96" viewBox="0 0 110 96" fill="none" stroke="#111" stroke-width="2.4">
    <circle cx="55" cy="48" r="44"/><circle cx="55" cy="48" r="32"/><circle cx="55" cy="48" r="14"/><circle cx="55" cy="48" r="5"/>
    <path d="M55 4 V16 M55 80 V92 M11 48 H23 M87 48 H99 M24 17 L32 25 M78 71 L86 79 M86 17 L78 25 M32 71 L24 79"/>
  </svg>
  <h3>Enter Service</h3>
  <p>Curabitur cursus sapien pharetra pretium suscipit. Etiam eu neque rhoncus, eleifend ex ut, ornare leo. Cras ac orci orci. Proin mattis nisi consequat</p>
</div>
<a class="btn" style="left:168px;top:2458px;width:160px">View More</a>
<a class="btn" style="left:521px;top:2458px;width:160px">View More</a>
<a class="btn" style="left:872px;top:2458px;width:160px">View More</a>

<!-- Jewelry -->
<p class="eyebrow abs center" style="left:0;width:1200px;top:2634px">Our Jewelry</p>
<h2 class="h2 abs center" style="left:0;width:1200px;top:2669px">Angel Number Jewelry</h2>
<p class="lead abs center" style="left:260px;width:680px;top:2733px">Lorem ipsum dolor sit amet, consectetur adipiscing elit. Donec nec egestas tellus, et condimentum est.</p>

<div class="jewel-card"></div>
<div class="jewel" style="left:94px"><div class="photo gold" role="img" aria-label="Rose gold angel pendant with crystal"></div><p class="name">Jewelry Name</p><p class="desc">Lorem ipsum dolor<br>sit amet</p><p class="cart">Add To Cart <svg width="14" height="10" viewBox="0 0 14 10"><path d="M0 5 H12 M8 1 L12 5 L8 9" fill="none" stroke="currentColor" stroke-width="1.5"/></svg></p></div>
<div class="jewel" style="left:358px"><div class="photo silver" role="img" aria-label="Silver cherub pendant"></div><p class="name">Jewelry Name</p><p class="desc">Lorem ipsum dolor<br>sit amet</p><p class="cart">Add To Cart <svg width="14" height="10" viewBox="0 0 14 10"><path d="M0 5 H12 M8 1 L12 5 L8 9" fill="none" stroke="currentColor" stroke-width="1.5"/></svg></p></div>
<div class="jewel on-light" style="left:622px"><div class="photo gold" role="img" aria-label="Rose gold angel pendant with crystal"></div><p class="name">Jewelry Name</p><p class="desc">Lorem ipsum dolor<br>sit amet</p><p class="cart">Add To Cart <svg width="14" height="10" viewBox="0 0 14 10"><path d="M0 5 H12 M8 1 L12 5 L8 9" fill="none" stroke="currentColor" stroke-width="1.5"/></svg></p></div>
<div class="jewel" style="left:886px"><div class="photo silver" role="img" aria-label="Silver cherub pendant"></div><p class="name">Jewelry Name</p><p class="desc">Lorem ipsum dolor<br>sit amet</p><p class="cart">Add To Cart <svg width="14" height="10" viewBox="0 0 14 10"><path d="M0 5 H12 M8 1 L12 5 L8 9" fill="none" stroke="currentColor" stroke-width="1.5"/></svg></p></div>

<!-- Contact -->
<div class="contact-bg"></div>
<div class="planet" role="img" aria-label="Glowing red and blue planet"></div>
<h2 class="h2 abs" style="left:85px;top:3367px">Get in Touch</h2>
<div class="field" style="left:85px">Name</div>
<div class="field" style="left:511px">Email</div>
<a class="btn" style="left:956px;top:3417px;width:159px">Get Notified</a>

<!-- Footer -->
<footer>
  <div class="footer-bg" role="img" aria-label="Deep space nebula"></div>
  <div class="brand-mark" style="left:528px;top:3621px;width:144px;height:144px">LunoVix</div>
  <p class="abs center" style="left:0;width:1200px;top:3792px;font-size:19px">LunoVix is zodiac signs &amp; angel number jewelry.</p>
  <div class="rule" style="top:3842px"></div>
  <div class="footer-links"><span>Home</span><span>About</span><span>Services</span><span>Contact</span></div>
  <div class="rule" style="top:3896px"></div>
  <p class="abs center" style="left:0;width:1200px;top:3928px;font-size:14px">© 2022. All Rights Reserved.</p>
  <div class="social abs" style="left:551px;top:3970px" aria-label="Social links"><span></span><span></span><span></span></div>
</footer>

</body>
</html>
```